Chiropractic healthcare group business card

We are a Portland Oregon based chiropractic healthcare group. Looking for a new business card design. Something cutting edge, that shows off our new logo and tag line.Use either of the attached logos.Our tag line = "Who would you be without pain?"I'm open to about anything, impress me!!
Target Market(s)
Chiropractic patients - Auto injury, back pain, sports injuries, neck , shoulder, hip, knee, ankle pain.
Industry/Entity Type
Chiropractic
Contact Information for Business Card
Dr. Bram Holtvick, D.C.
Clinic name - Fernway Chiropractic
2 clinics
location #1
20418 NW Marwick Road
Suite B
North Plains, OR 97133
Location #2
13529 SE Calloway Street
Portland OR 97236
Main phone line 971.555.0143
website : www.FernwayClinics.example
Tag line "Who would you be without pain?"
Colors
Designer to choose colors to be used in the design.
Requirements
Must have
- Use the logo colors -- Want the orange color to be a TRUE orange.
- Both clinic address
- phone number
- website
- personal email - b.holtvick@ReliefBeginsHere.example
- tag line - "Who would you be without pain?"

```html
<!DOCTYPE html>
<html lang="en">
<head>
<meta charset="utf-8">
<title>Fernway Chiropractic – Business Card</title>
<link rel="stylesheet" href="https://fonts.googleapis.com/css2?family=Montserrat:wght@400;500;600;700&display=swap">
<style>
  :root {
    --bg: #d6d6d6;
    --slate: #5a5b5d;
    --orange: #f7941d;
    --white: #ffffff;
    --ink: #4a4a4c;
    --card-w: 620px;
    --card-h: 355px;
  }
  * { box-sizing: border-box; margin: 0; padding: 0; }
  html, body { width: 1200px; height: 930px; overflow: hidden; }
  body {
    background: var(--bg);
    font-family: "Montserrat", Arial, sans-serif;
    position: relative;
  }
  .card {
    position: absolute;
    width: var(--card-w);
    height: var(--card-h);
    border-radius: 26px;
    overflow: hidden;
    box-shadow: 0 10px 24px rgba(0,0,0,0.18);
  }

  /* Front */
  .card-front {
    left: 80px; top: 60px;
    background: var(--slate);
    color: var(--white);
    display: flex; flex-direction: column; align-items: center; justify-content: center;
  }
  .brand {
    display: flex; align-items: center; gap: 14px;
    font-weight: 700; letter-spacing: 0.06em; text-transform: uppercase;
    white-space: nowrap;
  }
  .brand-mark { width: 18px; height: 18px; background: var(--orange); flex: none; }
  .card-front .brand { font-size: 30px; color: var(--white); }
  .tagline {
    margin-top: 70px;
    font-size: 19px; font-weight: 500; letter-spacing: 0.02em;
  }

  /* Back */
  .card-back { left: 500px; top: 505px; background: var(--white); }
  .card-back svg.backdrop { position: absolute; inset: 0; }
  .card-back .brand {
    position: absolute; right: 40px; top: 42px;
    font-size: 20px; color: var(--ink);
  }
  .doctor-name {
    position: absolute; left: 28px; top: 200px;
    font-size: 22px; font-weight: 600; color: var(--white);
    white-space: nowrap;
  }
  .locations {
    position: absolute; left: 372px; top: 190px;
    color: var(--white); font-size: 14px; line-height: 1.4;
    white-space: nowrap;
  }
  .locations address { font-style: normal; margin-bottom: 12px; }
  .contact {
    position: absolute; left: 28px; bottom: 26px;
    list-style: none; color: var(--white); font-size: 14px; line-height: 1.6;
    white-space: nowrap;
  }
  .contact li { display: flex; align-items: center; gap: 10px; }
  .contact svg { width: 12px; height: 12px; flex: none; }
</style>
</head>
<body>

<section class="card card-front" aria-label="Business card front">
  <div class="brand"><span class="brand-mark"></span>Fernway Chiropractic</div>
  <p class="tagline">Who would you be without pain?</p>
</section>

<section class="card card-back" aria-label="Business card back">
  <svg class="backdrop" viewBox="0 0 620 355" width="620" height="355" aria-hidden="true">
    <polygon points="0,240 290,240 300,190 620,150 620,355 0,355" fill="#5a5b5d"/>
    <polygon points="0,190 305,190 290,240 0,240" fill="#f7941d"/>
  </svg>

  <div class="brand"><span class="brand-mark"></span>Fernway Chiropractic</div>

  <h1 class="doctor-name">Dr. Bram Holtvick, D.C.</h1>

  <div class="locations">
    <address>20418 NW Marwick Road<br>Suite B<br>North Plains, OR 97133</address>
    <address>13529 SE Calloway Street<br>Portland OR 97236</address>
  </div>

  <ul class="contact">
    <li>
      <svg viewBox="0 0 24 24" fill="#ffffff"><path d="M6.6 10.8a15 15 0 0 0 6.6 6.6l2.2-2.2a1 1 0 0 1 1-.25 11.4 11.4 0 0 0 3.6.57 1 1 0 0 1 1 1V20a1 1 0 0 1-1 1A17 17 0 0 1 3 4a1 1 0 0 1 1-1h3.5a1 1 0 0 1 1 1c0 1.25.2 2.45.57 3.57a1 1 0 0 1-.25 1z"/></svg>
      971.555.0143
    </li>
    <li>
      <svg viewBox="0 0 24 24" fill="none" stroke="#ffffff" stroke-width="2.4"><rect x="2" y="5" width="20" height="14" rx="1"/><path d="M2 6l10 7 10-7"/></svg>
      b.holtvick@ReliefBeginsHere.example
    </li>
    <li>
      <svg viewBox="0 0 24 24" fill="none" stroke="#ffffff" stroke-width="2.2"><circle cx="12" cy="12" r="10"/><path d="M2 12h20M12 2a15 15 0 0 1 0 20M12 2a15 15 0 0 0 0 20"/></svg>
      www.FernwayClinics.example
    </li>
  </ul>
</section>

</body>
</html>
```